Powerpoint for Swimming Certification Course Content

We have created a swim lesson teacher certification course and need a powerpoint presentation for the content that we are presenting on. We are looking for fun and playful designs, but still look professional as this will be a certification course. Please keep all pictures and images that have been included on the slides attached. You can reformat them or recreate them to match color schemes, but please do not remove them as they will be key to the content. If slides do not have pictures or images, please add in a picture or an image as we will go back in later and replace the image if necessary with our own personal ones. I have attached the certification logo to help provide ideas for the color scheme. Feel free to modify that image as necessary.

```html
<!DOCTYPE html>
<html lang="en">
<head>
<meta charset="utf-8">
<title>Role of the Aquatic Educator – Slides</title>
<link rel="stylesheet" href="https://fonts.googleapis.com/css2?family=Cabin:wght@400;600&family=Mali:wght@500&display=swap">
<style>
  :root {
    --stage: #000000;
    --slide-base: #eefafc;
    --wave-light: #d9f5fa;
    --wave-mid: #e5f8fb;
    --wave-white: #ffffff;
    --title-blue: #2f4f96;
    --ink: #1b1b1b;
    --brand-teal: #1aa7a8;
    --water-deep: #4f8fd0;
    --water-mid: #9cc7ee;
    --water-pale: #f4fbff;
    --splash-grey: #c9cdd2;
  }
  * { box-sizing: border-box; margin: 0; padding: 0; }
  html, body { width: 1200px; height: 1200px; overflow: hidden; background: var(--stage); }
  .canvas { position: relative; width: 1200px; height: 1200px; background: var(--stage); }

  .slide {
    position: absolute; left: 182px; width: 839px; height: 472px;
    background: var(--slide-base); overflow: hidden;
  }
  .slide--intro { top: 102px; }
  .slide--duties { top: 627px; }
  .slide__waves { position: absolute; inset: 0; width: 100%; height: 100%; }

  .slide__title {
    position: absolute; left: 69px; top: 28px;
    font-family: "Cabin", sans-serif; font-weight: 600; font-size: 27px;
    color: var(--title-blue); letter-spacing: 0.2px;
  }

  .water-orb {
    position: absolute; border-radius: 50%;
    background: radial-gradient(circle at 50% 50%, var(--water-pale) 0%, #dcecf9 45%, var(--water-mid) 72%, var(--water-deep) 92%, rgba(79,143,208,0) 100%);
    box-shadow: 0 0 40px 14px rgba(120,140,160,0.25);
  }
  .water-swirl {
    position: absolute; border-radius: 50%;
    background: radial-gradient(circle at 50% 50%, #ffffff 0%, #ffffff 22%, var(--water-deep) 30%, var(--water-mid) 42%, var(--splash-grey) 60%, rgba(201,205,210,0.5) 78%, rgba(201,205,210,0) 100%);
  }
  .orb-label {
    position: absolute; text-align: center;
    font-family: "Mali", cursive; font-weight: 500; color: var(--ink);
    line-height: 1.55; transform: translate(-50%, -50%); white-space: nowrap;
  }

  .brand {
    position: absolute; left: 691px; top: 404px;
    display: flex; align-items: center; gap: 6px;
  }
  .brand__dot {
    width: 50px; height: 50px; border-radius: 50%;
    border: 2px solid var(--brand-teal); background: transparent;
  }
  .brand__name {
    font-family: "Cabin", sans-serif; font-weight: 400; font-size: 13px;
    line-height: 1.3; color: var(--brand-teal);
  }

  .duty-list {
    position: absolute; left: 451px; top: 100px; list-style: none;
    font-family: "Cabin", sans-serif; font-size: 17.5px; color: var(--ink);
    letter-spacing: 0.3px;
  }
  .duty-list li { height: 45.5px; line-height: 24px; }
</style>
</head>
<body>
<main class="canvas">

  <section class="slide slide--intro">
    <svg class="slide__waves" viewBox="0 0 839 472" preserveAspectRatio="none" aria-hidden="true">
      <path d="M0 0 H839 V60 C700 20 560 110 420 90 C260 70 160 20 0 70 Z" fill="var(--wave-light)"/>
      <path d="M0 70 C160 20 260 70 420 90 C560 110 700 20 839 60 V110 C700 60 560 140 420 125 C250 110 150 60 0 110 Z" fill="var(--wave-mid)"/>
      <path d="M0 400 C80 430 150 460 200 472 H0 Z" fill="var(--wave-mid)"/>
      <path d="M540 472 C640 430 740 380 839 370 V472 Z" fill="var(--wave-white)"/>
    </svg>
    <h1 class="slide__title">Role of the Aquatic Educator</h1>

    <div class="water-orb" role="img" aria-label="Sphere of splashing water" style="left:120px; top:162px; width:166px; height:166px;"></div>
    <p class="orb-label" style="left:203px; top:245px; font-size:23px;">Swim<br>Teacher</p>

    <div class="water-swirl" role="img" aria-label="Swirling water splash forming a ring" style="left:371px; top:82px; width:386px; height:343px;"></div>
    <p class="orb-label" style="left:564px; top:254px; font-size:24px;">Aquatic<br>Educator</p>

    <div class="brand">
      <span class="brand__dot"></span>
      <span class="brand__name">Ripple<br>Swim<br>Institute</span>
    </div>
  </section>

  <section class="slide slide--duties">
    <svg class="slide__waves" viewBox="0 0 839 472" preserveAspectRatio="none" aria-hidden="true">
      <path d="M0 0 H839 V60 C700 20 560 110 420 90 C260 70 160 20 0 70 Z" fill="var(--wave-light)"/>
      <path d="M0 70 C160 20 260 70 420 90 C560 110 700 20 839 60 V110 C700 60 560 140 420 125 C250 110 150 60 0 110 Z" fill="var(--wave-mid)"/>
      <path d="M0 400 C80 430 150 460 200 472 H0 Z" fill="var(--wave-mid)"/>
      <path d="M540 472 C640 430 740 380 839 370 V472 Z" fill="var(--wave-white)"/>
    </svg>

    <div class="water-orb" role="img" aria-label="Sphere of splashing water" style="left:138px; top:163px; width:184px; height:184px;"></div>
    <p class="orb-label" style="left:230px; top:255px; font-size:27px;">Swim<br>Teacher</p>

    <ul class="duty-list">
      <li>Teaching skill based activities</li>
      <li>Planning and preparing lessons</li>
      <li>Delivering fun and inclusive lessons</li>
      <li>Monitoring and recording progress</li>
      <li>Teaching safety skills</li>
      <li>Supporting progress</li>
    </ul>

    <div class="brand">
      <span class="brand__dot"></span>
      <span class="brand__name">Ripple<br>Swim<br>Institute</span>
    </div>
  </section>

</main>
</body>
</html>
```